Newsletter Banner Ad with a URL to our website offering

We need a banner ad for a newsletter that is published to members biweekly that simply articulates our value proposition and enables the reader to click on our logo to learn more and engage with us to schedule an Emergency Response Plan so they are ready for when a burst pipe happens on their property. They will have a plan after they engage with us.
We need quotes to build two options 1&2

```html
<!DOCTYPE html>
<html lang="en">
<head>
<meta charset="utf-8">
<title>Rapid Response Plan Banners – Ridgeway Property Restoration</title>
<link rel="stylesheet" href="https://fonts.googleapis.com/css2?family=Anton&display=swap">
<style>
  :root {
    --page: #ffffff;
    --red-deep: #d3112e;
    --red-main: #ec1427;
    --blue-deep: #0a3db4;
    --blue-main: #0145ff;
    --ink: #1d1d22;
    --white: #ffffff;
    --mark-blue: #2a4fb0;
  }
  * { margin: 0; padding: 0; box-sizing: border-box; }
  html, body {
    width: 1200px; height: 732px; overflow: hidden;
    background: var(--page);
  }
  .canvas { position: relative; width: 1200px; height: 732px; }
  .banner {
    position: absolute;
    width: 1004px; height: 260px;
    overflow: hidden;
  }
  .banner--red { left: 97px; top: 82px; }
  .banner--blue { left: 101px; top: 397px; }
  .banner__art { position: absolute; inset: 0; width: 100%; height: 100%; }
  .banner__headline {
    position: absolute;
    left: 72px; top: 53px; width: 400px;
    font-family: "Anton", "Impact", sans-serif;
    font-weight: 400;
    font-size: 45px;
    line-height: 50px;
    color: var(--white);
    text-align: center;
    letter-spacing: 0.2px;
  }
  .banner__headline .first-line { padding-left: 56px; display: block; }
  .brand {
    position: absolute;
    left: 858px; top: 162px; width: 114px;
    text-align: center;
    font-family: "Anton", "Impact", sans-serif;
    color: var(--ink);
    text-decoration: none;
  }
  .brand__dot {
    display: block; width: 30px; height: 30px; margin: 0 auto 10px;
    border-radius: 50%; background: var(--mark-blue);
  }
  .brand__name { display: block; font-size: 17px; line-height: 18px; letter-spacing: 2.4px; }
  .brand__tagline { display: block; font-size: 7px; line-height: 10px; letter-spacing: 1px; }
</style>
</head>
<body>
<main class="canvas">

  <!-- Option 1: red -->
  <section class="banner banner--red">
    <svg class="banner__art" viewBox="0 0 1740 450" preserveAspectRatio="none">
      <defs>
        <linearGradient id="corridor-tones" x1="0" y1="0" x2="0" y2="1">
          <stop offset="0" stop-color="#8f9093"/>
          <stop offset="0.35" stop-color="#a6a4a6"/>
          <stop offset="0.6" stop-color="#8b6f77"/>
          <stop offset="1" stop-color="#c9455c"/>
        </linearGradient>
      </defs>
      <rect x="780" y="0" width="960" height="450" fill="url(#corridor-tones)"
            role="img" aria-label="Photo of a flooded hospital corridor with water across the floor"/>
      <path d="M0,0 H835 C920,120 966,300 966,450 H0 Z" fill="var(--red-deep)"/>
      <path d="M30,0 H780 C880,110 940,290 940,450 H110 C30,370 0,200 30,0 Z" fill="var(--red-main)"/>
      <g fill="var(--white)">
        <path d="M98,56 H128 V113 H71 V85 H98 Z"/>
        <path d="M155,114 H185 V171 H128 V142 H155 Z"/>
      </g>
      <circle cx="1592" cy="418" r="200" fill="var(--white)"/>
    </svg>
    <h2 class="banner__headline">
      <span class="first-line">Do you have a</span>
      rapid response plan<br>for this ?
    </h2>
    <a class="brand" href="#">
      <span class="brand__dot"></span>
      <span class="brand__name">RIDGEWAY</span>
      <span class="brand__tagline">PROPERTY RESTORATION</span>
    </a>
  </section>

  <!-- Option 2: blue -->
  <section class="banner banner--blue">
    <svg class="banner__art" viewBox="0 0 1740 450" preserveAspectRatio="none">
      <defs>
        <linearGradient id="spray-tones" x1="0" y1="0" x2="1" y2="0.4">
          <stop offset="0" stop-color="#5a5650"/>
          <stop offset="0.3" stop-color="#b9a58a"/>
          <stop offset="0.6" stop-color="#9a8f82"/>
          <stop offset="0.85" stop-color="#f4e7c8"/>
          <stop offset="1" stop-color="#b5652c"/>
        </linearGradient>
      </defs>
      <rect x="780" y="0" width="960" height="450" fill="url(#spray-tones)"
            role="img" aria-label="Photo of water spraying from a burst pipe between wall studs"/>
      <path d="M0,0 H835 C920,120 966,300 966,450 H0 Z" fill="var(--blue-deep)"/>
      <path d="M30,0 H780 C880,110 940,290 940,450 H110 C30,370 0,200 30,0 Z" fill="var(--blue-main)"/>
      <g stroke="var(--white)" stroke-width="5" stroke-linecap="round">
        <line x1="123" y1="88" x2="123" y2="60"/>
        <line x1="135.5" y1="91.3" x2="149.5" y2="67.1"/>
        <line x1="144.7" y1="100.5" x2="168.9" y2="86.5"/>
        <line x1="148" y1="113" x2="176" y2="113"/>
        <line x1="144.7" y1="125.5" x2="168.9" y2="139.5"/>
        <line x1="135.5" y1="134.7" x2="149.5" y2="158.9"/>
        <line x1="123" y1="138" x2="123" y2="166"/>
        <line x1="110.5" y1="134.7" x2="96.5" y2="158.9"/>
        <line x1="101.3" y1="125.5" x2="77.1" y2="139.5"/>
        <line x1="98" y1="113" x2="70" y2="113"/>
        <line x1="101.3" y1="100.5" x2="77.1" y2="86.5"/>
        <line x1="110.5" y1="91.3" x2="96.5" y2="67.1"/>
      </g>
      <circle cx="1592" cy="418" r="200" fill="var(--white)"/>
    </svg>
    <h2 class="banner__headline">
      <span class="first-line">Do you have a</span>
      rapid response plan<br>for this ?
    </h2>
    <a class="brand" href="#">
      <span class="brand__dot"></span>
      <span class="brand__name">RIDGEWAY</span>
      <span class="brand__tagline">PROPERTY RESTORATION</span>
    </a>
  </section>

</main>
</body>
</html>
```